KORVAN TECH LTD

Advertisement to get more schools:
use website https://www.korvan-tech.co.uk for logos etc.
ICT Service Level Agreements for as little as £2000 per year
Unlimited Remote, phone and email support
Unlimited Call outs included
90% fix time within 30 minutes of ticket submission
Extra support during Quadrel inspections
GDPR service included

```html
<!DOCTYPE html>
<html lang="en">
<head>
<meta charset="utf-8">
<title>Korvan Tech – ICT SLA Advertisement</title>
<link rel="stylesheet" href="https://fonts.googleapis.com/css2?family=Roboto:wght@700;900&family=Signika:wght@400;500;600&display=swap">
<style>
  :root {
    --blue-deep: #0b4fa8;
    --blue-main: #1572cf;
    --blue-bright: #1e8ee0;
    --blue-footer: #1a86cc;
    --orange: #f7894f;
    --orange-strong: #f26a25;
    --ink: #1c1c1c;
    --pale: #eef5fb;
    --white: #ffffff;
    --placeholder-yellow: #eed43a;
  }
  * { box-sizing: border-box; margin: 0; padding: 0; }
  html, body {
    width: 686px; height: 1200px; overflow: hidden;
    background: var(--white);
  }
  .ad {
    position: absolute; left: 0; top: 118px;
    width: 686px; height: 964px; overflow: hidden;
    background: linear-gradient(180deg, #ffffff 0%, var(--pale) 55%, #ffffff 100%);
    font-family: "Signika", sans-serif;
  }
  .header-band {
    position: absolute; left: 0; top: 0; width: 686px; height: 326px;
    background: linear-gradient(160deg, #0a5cc0 0%, var(--blue-main) 45%, #0d4e9e 100%);
  }
  .brand {
    position: absolute; left: 0; top: 50px; width: 734px;
    text-align: center; color: var(--white);
  }
  .brand-name {
    font-family: "Signika", sans-serif; font-weight: 600;
    font-size: 40px; letter-spacing: 2px; line-height: 1;
  }
  .brand-tagline {
    display: inline-block; margin-top: 8px; padding-top: 5px;
    border-top: 1px solid rgba(255,255,255,0.8);
    font-size: 12.5px; letter-spacing: 1.2px; font-weight: 500;
  }
  .photo-frame {
    position: absolute; left: 59px; top: 149px; width: 571px; height: 282px;
    background: var(--white); border-radius: 30px;
    border-bottom: 4px solid var(--orange-strong);
    border-top: 3px solid var(--orange-strong);
    padding: 6px;
  }
  .photo {
    width: 100%; height: 100%; border-radius: 24px;
    background: linear-gradient(100deg, #3f8fc4 0%, #d8678e 28%, #2f8f5a 55%, #6cc9d8 80%, #e8e8e8 100%);
  }
  .headline {
    position: absolute; left: 0; width: 686px; text-align: center;
    font-family: "Roboto", sans-serif; line-height: 1;
  }
  .headline-lead {
    top: 455px; font-weight: 700; font-size: 33.5px; color: var(--blue-main);
    letter-spacing: -0.3px;
  }
  .headline-price {
    top: 490px; font-weight: 900; font-size: 52px; color: var(--orange);
    letter-spacing: 5px;
  }
  .device-placeholder {
    position: absolute; left: 78px; top: 572px; width: 64px; height: 150px;
    z-index: 2;
    background: linear-gradient(180deg, var(--placeholder-yellow) 0%, #e2c428 100%);
  }
  .support-banner {
    position: absolute; left: 123px; top: 573px; width: 340px; height: 126px;
    background: var(--orange);
    clip-path: polygon(0 0, 100% 0, 94% 100%, 0 100%);
    color: var(--white); font-weight: 500; font-size: 31px; line-height: 1.1;
    padding: 14px 0 0 40px;
  }
  .callout-badge {
    position: absolute; left: 437px; top: 550px; width: 184px; height: 184px;
    border-radius: 50%; background: var(--blue-main);
    border: 4px solid var(--white);
    display: flex; align-items: center; justify-content: center; text-align: center;
    color: var(--white); font-weight: 600; font-size: 28px; line-height: 1.15;
  }
  .features {
    position: absolute; left: 58px; top: 746px; list-style: none;
    font-size: 22.5px; color: var(--ink); line-height: 1.17;
  }
  .features li { position: relative; padding-left: 31px; margin-bottom: 14px; }
  .features svg { position: absolute; left: 0; top: 5px; }
  .fix-time {
    position: absolute; left: 411px; top: 748px; color: var(--ink); line-height: 1.1;
  }
  .fix-time-figure { color: var(--orange); font-weight: 500; font-size: 39.5px; }
  .fix-time-detail { font-size: 27px; line-height: 1.05; }
  .footer-band {
    position: absolute; left: 0; top: 857px; width: 686px; height: 107px;
    background: linear-gradient(180deg, var(--blue-footer) 0%, #1469c0 100%);
    color: var(--white);
  }
  .contact {
    position: absolute; top: 21px; left: 55px; display: flex; align-items: center;
    font-family: "Signika", sans-serif; font-weight: 500; font-size: 23px;
  }
  .divider { width: 2px; height: 28px; background: var(--white); margin: 0 17px; }
  .social { display: flex; gap: 17px; }
  .social span {
    width: 29px; height: 29px; border-radius: 50%; border: 2px solid var(--white);
  }
</style>
</head>
<body>
<main class="ad">
  <div class="header-band" role="img" aria-label="Blue background with technology icons"></div>

  <div class="brand">
    <div class="brand-name">KORVAN TECH</div>
    <div class="brand-tagline">EDUCATION SUPPORT &amp; INSTALLATION</div>
  </div>

  <div class="photo-frame">
    <div class="photo" role="img" aria-label="Photo of four school children looking at a tablet together"></div>
  </div>

  <h1 class="headline headline-lead">ICT SLA AGREEMENTS FOR AS LITTLE</h1>
  <p class="headline headline-price">AS £2000 PER YEAR</p>

  <div class="support-banner">Unlimited Remote,<br>phone and email<br>support</div>
  <div class="device-placeholder" role="img" aria-label="Image of a yellow smartphone"></div>

  <div class="callout-badge">UNLIMITED<br>CALL OUTS<br>INCLUDED</div>

  <ul class="features">
    <li>
      <svg width="21" height="21" viewBox="0 0 21 21"><circle cx="10.5" cy="10.5" r="10" fill="#1e7fe6"/><path d="M5.5 11 L9 14.5 L15.5 7" fill="none" stroke="#fff" stroke-width="2.4" stroke-linecap="round" stroke-linejoin="round"/></svg>
      Extra support during Quadrel<br>inspections
    </li>
    <li>
      <svg width="21" height="21" viewBox="0 0 21 21"><circle cx="10.5" cy="10.5" r="10" fill="#1e7fe6"/><path d="M5.5 11 L9 14.5 L15.5 7" fill="none" stroke="#fff" stroke-width="2.4" stroke-linecap="round" stroke-linejoin="round"/></svg>
      GDPR service included
    </li>
  </ul>

  <div class="fix-time">
    <div class="fix-time-figure">90% fix time</div>
    <div class="fix-time-detail">within 30 minutes<br>of ticket submission</div>
  </div>

  <footer class="footer-band">
    <div class="contact">
      <span class="phone">0161 555 0182</span>
      <span class="divider"></span>
      <span class="website">www.korvan-tech.co.uk</span>
      <span class="divider"></span>
      <span class="social"><span></span><span></span><span></span></span>
    </div>
  </footer>
</main>
</body>
</html>
```